Byte Crew - Settle Inn

A flyer to promote a service by Byte Crew that provides IT set up in home when moving house.

It should be for print format (A4, A5 and an email friendly version)

Logos, previous flyer, image all attached.

Please use black, green and white as base colours.Please change boys sweater/jumper in the photo to green to match the logo.

Byte Crew are bring a helpdesk to your front door, saving you time and money. With a variety of packages to suit your needs, the Byte Crew aims to tackle both small and complex issues from setting up a home network to servicing the needs of a growing company.

Target Market(s)

Consumers moving house, Relocation agents, Real Estate agents

Requirements
Must have
• Logo, image, text all attached
• Use of green, black and white
Nice to have
• Also have coloured ties if you want them for design

```html
<!DOCTYPE html>
<html lang="en">
<head>
<meta charset="utf-8">
<title>Byte Crew – Settle Inn flyer</title>
<link href="https://fonts.googleapis.com/css2?family=Open+Sans:wght@700;800&family=PT+Sans+Narrow:wght@700&family=PT+Serif&display=swap" rel="stylesheet">
<style>
  :root {
    --ink: #000;
    --paper: #fff;
    --green: #8dc63f;
    --green-text: #a3cf4e;
    --panel: #0d0d0d;
  }
  html, body { margin: 0; padding: 0; overflow: hidden; background: var(--ink); }
  .flyer {
    position: relative; width: 933px; height: 1200px; overflow: hidden;
    background: var(--ink); color: var(--paper);
    font-family: "Open Sans", Arial, sans-serif;
  }
  .hero-photo {
    position: absolute; left: 222px; top: 0; width: 472px; height: 422px;
    background: linear-gradient(180deg, #6b4a30 0%, #c49a7c 30%, #d8b49a 52%, #7b8d86 70%, #8dc63f 100%);
  }
  .headline {
    position: absolute; left: 44px; top: 72px; margin: 0;
    font-weight: 800; line-height: 0.95; letter-spacing: -1px;
  }
  .headline .do { font-size: 50px; vertical-align: 14px; }
  .headline .not { font-size: 82px; }
  .headline .fear { display: block; padding-left: 96px; font-size: 62px; }
  .brand-panel {
    position: absolute; left: 616px; top: 56px; width: 317px; height: 250px;
    background: var(--panel);
  }
  .brand-panel .the { position: absolute; left: 10px; top: 42px; font-size: 40px; font-weight: 800; }
  .brand-panel .name {
    position: absolute; left: 10px; top: 98px; font-size: 56px; font-weight: 800;
    letter-spacing: -1px; color: var(--paper); white-space: nowrap;
  }
  .brand-panel .here { position: absolute; left: 88px; top: 188px; font-size: 40px; font-weight: 800; }
  .question {
    position: absolute; left: 0; top: 428px; width: 933px; margin: 0; text-align: center;
    font-family: "PT Sans Narrow", Arial, sans-serif; font-size: 31px; font-weight: 700;
  }
  .pitch {
    position: absolute; left: 0; top: 474px; width: 933px; margin: 0; text-align: center;
    color: var(--green-text); font-size: 21px; font-weight: 700; line-height: 31px;
  }
  .package {
    position: absolute; left: 39px; top: 544px; width: 845px; height: 482px;
    border: 5px solid var(--green);
  }
  .package h2 {
    margin: 14px 0 0; text-align: center; font-size: 38px; font-weight: 700; line-height: 44px;
  }
  .features {
    position: absolute; top: 62px; width: 400px; margin: 0; padding: 0; list-style: none;
    font-family: "PT Serif", Georgia, serif; font-size: 22px; line-height: 30px; color: var(--green-text);
  }
  .features li::before { content: "-  "; }
  .features.left { left: 20px; }
  .features.right { left: 435px; }
  .footnote {
    position: absolute; top: 418px; margin: 0; width: 400px;
    font-family: "PT Serif", Georgia, serif; font-size: 14px; line-height: 18px; color: var(--paper);
  }
  .footnote.left { left: 20px; }
  .footnote.right { left: 435px; }
  .cta {
    position: absolute; left: 0; top: 1036px; width: 933px; margin: 0; text-align: center;
    font-size: 60px; font-weight: 800; line-height: 70px;
  }
  .contact {
    position: absolute; left: 0; top: 1100px; width: 933px; margin: 0; text-align: center;
    font-size: 16px; line-height: 22px;
    font-family: "Open Sans", Arial, sans-serif; font-weight: 700;
  }
</style>
</head>
<body>
<main class="flyer">
  <div class="hero-photo" role="img" aria-label="Photo of a worried boy in glasses and a green sweater holding up a green network cable"></div>

  <h1 class="headline"><span class="do">Do </span><span class="not">NOT</span><span class="fear">FEAR...</span></h1>

  <div class="brand-panel">
    <span class="the">The</span>
    <span class="name">Byte Crew</span>
    <span class="here">is Here!</span>
  </div>

  <p class="question">Can’t Remember What To Plug In Where?</p>
  <p class="pitch">We take all the pain out of moving house and get you set-up,<br>online and connected before you can say the word Geek.</p>

  <section class="package">
    <h2>Welcome Home Crew $425</h2>
    <ul class="features left">
      <li>Pre-visit online assessment to ensure maximum use of our Geek’s time</li>
      <li>Ready:&nbsp; IT Health Check and Audit Report</li>
      <li>Set:&nbsp; Connection of your wireless network for user access including passwords and parental control if desired</li>
      <li>Expanding the family: Connection of one additional device eg media box, tablet, game console, Smart TV*</li>
      <li>Byte Crew Membership</li>
    </ul>
    <ul class="features right">
      <li>Updating of software and virus security check</li>
      <li>Ready:&nbsp; IT Health Check and Audit Report</li>
      <li>Includes travel cost and up to 4 hours of a Geek’s time in your house</li>
      <li>1 month free on Crew@Home Packages**</li>
      <li>Awesome Byte Crew fridge magnet</li>
      <li>Go: Set up of 3 computers and 1 printer</li>
    </ul>
    <p class="footnote left">*Each additional device set-up is charged at $35</p>
    <p class="footnote right">** Based on our annual packages and If signed within 14 days</p>
  </section>

  <p class="cta">Book Now!</p>
  <p class="contact">www.bytecrew.asia<br>Email booking@bytecrew.asia<br>Hotline 6612 3490</p>
</main>
</body>
</html>
```